Looking for a brindle ebook cover. Must meet all brindle press platform specifics. *

I need a book cover for my romance novel. The title is "Hearts, Unspoken". I would like this in typographic and an illustration below ( as a reference you can see Tall Tales by Doreen Platt). The author name is T V Nel. The story is set in England in the countryside, during fall and winter. It is a love/coming of age novel about a young couple. The girl is a writer, the boy is overcoming illness. The ending is tragic. The tone of the cover should convey an emotional read about true love and separation. It is a book for readers who enjoy novels by Bibi Tarns, Rosalind Voss, Doreen Platt.

Target Market(s)

Women in their 20s and 30s who enjoy romance.

Industry/Entity Type

Publishing

Font styles to use
Sans Serif

Requirements
Must have
• You can stress the title more than the author name on the cover.
Should not have
• No photographs.

```html
<!DOCTYPE html>
<html lang="en">
<head>
<meta charset="utf-8">
<title>Hearts, Unspoken — T V Nel</title>
<link href="https://fonts.googleapis.com/css2?family=Abril+Fatface&family=Cinzel:wght@400&family=Great+Vibes&display=swap" rel="stylesheet">
<style>
  :root {
    --paper-light: #f8f8f9;
    --paper-mid: #e3e3e5;
    --paper-shade: #cdced1;
    --ink: #2f2f31;
    --glint: rgba(255, 255, 255, 0.55);
  }
  html, body {
    margin: 0;
    padding: 0;
    width: 848px;
    height: 1200px;
    overflow: hidden;
    background: var(--paper-mid);
  }
  .cover {
    position: relative;
    width: 848px;
    height: 1200px;
    overflow: hidden;
    background:
      radial-gradient(circle at 70% 15%, var(--glint) 0 3%, transparent 4%),
      radial-gradient(circle at 18% 42%, var(--glint) 0 2.5%, transparent 3.5%),
      radial-gradient(circle at 85% 62%, var(--glint) 0 4%, transparent 5.5%),
      radial-gradient(circle at 10% 70%, var(--glint) 0 2%, transparent 3%),
      radial-gradient(ellipse at 50% 45%, var(--paper-light) 0%, var(--paper-mid) 60%, var(--paper-shade) 100%);
  }
  .snow-drift {
    position: absolute;
    left: 0;
    bottom: 0;
    width: 100%;
    height: 200px;
    background: linear-gradient(to bottom, rgba(255,255,255,0) 0%, rgba(255,255,255,0.8) 55%, #fbfbfb 100%);
  }
  .title-art {
    position: absolute;
    top: 0;
    left: 0;
    width: 848px;
    height: 1200px;
  }
  .title-letters {
    font-family: "Abril Fatface", serif;
    font-size: 470px;
  }
  .title-script {
    font-family: "Great Vibes", cursive;
    font-size: 132px;
    fill: var(--ink);
  }
  .kicker {
    position: absolute;
    top: 108px;
    left: 0;
    width: 100%;
    margin: 0;
    text-align: center;
    font-family: "Cinzel", serif;
    font-size: 24px;
    letter-spacing: 22px;
    padding-left: 22px;
    box-sizing: border-box;
    color: var(--ink);
  }
  .author {
    position: absolute;
    top: 1076px;
    left: 0;
    width: 100%;
    margin: 0;
    text-align: center;
    font-family: "Cinzel", serif;
    font-size: 27px;
    letter-spacing: 14px;
    padding-left: 14px;
    box-sizing: border-box;
    color: var(--ink);
  }
  h1 { margin: 0; }
</style>
</head>
<body>
  <main class="cover">
    <div class="snow-drift"></div>
    <p class="kicker">A NOVEL</p>
    <h1 aria-label="Hearts, Unspoken">
      <svg class="title-art" viewBox="0 0 848 1200" aria-hidden="false">
        <defs>
          <linearGradient id="sky-fill" gradientUnits="userSpaceOnUse" x1="0" y1="172" x2="0" y2="496">
            <stop offset="0" stop-color="#5b91c5"/>
            <stop offset="0.4" stop-color="#9fb9cf"/>
            <stop offset="0.7" stop-color="#e6d6b0"/>
            <stop offset="0.88" stop-color="#f0dba6"/>
            <stop offset="1" stop-color="#6c6a5c"/>
          </linearGradient>
          <linearGradient id="meadow-fill" gradientUnits="userSpaceOnUse" x1="0" y1="516" x2="0" y2="838">
            <stop offset="0" stop-color="#8a7a4e"/>
            <stop offset="0.28" stop-color="#c99c55"/>
            <stop offset="0.5" stop-color="#9aa447"/>
            <stop offset="0.75" stop-color="#4f7f2c"/>
            <stop offset="1" stop-color="#2b5420"/>
          </linearGradient>
        </defs>
        <g class="title-letters" role="img" aria-label="Large letters HEARTS filled with a sky over distant hills above a misty golden meadow">
          <text x="125" y="496" fill="url(#sky-fill)" textLength="592" lengthAdjust="spacingAndGlyphs">HEA</text>
          <text x="110" y="838" fill="url(#meadow-fill)" textLength="606" lengthAdjust="spacingAndGlyphs">RTS</text>
        </g>
        <text class="title-script" x="424" y="948" text-anchor="middle" textLength="460" lengthAdjust="spacingAndGlyphs">unspoken</text>
      </svg>
    </h1>
    <p class="author">T V NEL</p>
  </main>
</body>
</html>
```